Business card design for Automotive workshop

We need a business card for a new automotive repair and tyre shop called Ridgeback Prime Automotive located in New Zealand. We are a clean, modern and fresh workshop and company.

Front needs to feature logo,
my name:
Lachie Westergaard (director)

Address:
48 Marlow Lane
Whitianga 3510

Phone: 07 842 1937
Mobile: 027 519 2764
Email: office@ridgebackmotors.co.nz
Website: ridgebackmotors.co.nz

Back needs to feature an area to write down appointment details, date and time.

Also feature a list of jobs and work we do such as,
Vehicle Servicing
All Mechanical Repairs
Warrant of Fitness
Tyres & Wheel Alignments
Automotive Diagnostics
Automotive Parts & Supplies

```html
<!DOCTYPE html>
<html lang="en">
<head>
<meta charset="utf-8">
<title>Ridgeback Prime Automotive – Business Card</title>
<link href="https://fonts.googleapis.com/css2?family=Lato:ital,wght@0,400;0,700;0,900;1,400;1,700&display=swap" rel="stylesheet">
<style>
  :root {
    --red: #d71f27;
    --black: #0b0b0b;
    --white: #ffffff;
    --paper: #f2f2f2;
    --ink: #1a1a1a;
    --stage: #cfcfcf;
  }
  * { box-sizing: border-box; margin: 0; padding: 0; }
  html, body { width: 1200px; height: 675px; overflow: hidden; }
  body {
    background: var(--stage);
    font-family: "Lato", sans-serif;
    position: relative;
  }
  .card {
    position: absolute;
    top: 183px;
    width: 540px;
    height: 309px;
    overflow: hidden;
    box-shadow: 0 6px 18px rgba(0,0,0,0.25);
  }

  /* ---------- Appointment side ---------- */
  .card-appointment {
    left: 40px;
    background: linear-gradient(180deg, var(--white) 0%, var(--paper) 100%);
    color: var(--ink);
  }
  .brand {
    position: absolute;
    display: flex;
    align-items: center;
    gap: 8px;
    font-weight: 900;
    text-transform: uppercase;
    line-height: 1;
    white-space: nowrap;
  }
  .brand-mark { width: 12px; height: 12px; background: var(--red); flex: none; }
  .brand-name { font-size: 19px; letter-spacing: 0.5px; }
  .card-appointment .brand { left: 26px; top: 30px; color: var(--red); }

  .services {
    position: absolute;
    right: 24px;
    top: 22px;
    list-style: none;
    font-style: italic;
    font-size: 11.5px;
    line-height: 16px;
  }
  .services li { position: relative; padding-left: 10px; }
  .services li::before {
    content: "";
    position: absolute; left: 0; top: 6px;
    width: 4px; height: 4px; border-radius: 50%;
    background: var(--red);
  }

  .appointment-title {
    position: absolute;
    left: 26px; top: 92px;
    color: var(--red);
    font-size: 15px;
    font-weight: 400;
    letter-spacing: 0.3px;
  }
  .field {
    position: absolute;
    display: flex;
    align-items: flex-end;
    font-size: 12px;
    height: 16px;
  }
  .field .line {
    flex: 1;
    border-bottom: 1.5px dotted var(--ink);
    margin-left: 3px;
    margin-bottom: 3px;
  }
  .field-name { left: 26px; right: 24px; top: 124px; }
  .field-time { left: 26px; width: 160px; top: 150px; }
  .ampm { position: absolute; left: 194px; top: 150px; display: flex; gap: 10px; font-size: 12px; }
  .field-date { left: 322px; right: 24px; top: 150px; }

  .check { display: inline-flex; align-items: center; gap: 3px; font-size: 12px; text-transform: uppercase; }
  .check::before {
    content: "";
    width: 9px; height: 9px;
    border: 1.5px solid var(--ink);
  }
  .days {
    position: absolute;
    left: 26px; right: 24px; top: 186px;
    display: flex;
    justify-content: space-between;
  }
  .days .check:nth-child(even) { margin-top: 16px; }

  .notice-band {
    position: absolute;
    left: 0; right: 0; bottom: 0;
    height: 58px;
    background: var(--red);
    color: var(--white);
    font-style: italic;
    font-size: 13px;
    display: flex;
    align-items: center;
    justify-content: center;
    padding-top: 10px;
  }

  /* ---------- Contact side ---------- */
  .card-contact {
    left: 620px;
    background: var(--black);
    color: var(--white);
    border: 2px solid var(--red);
  }
  .card-contact .brand {
    left: 24px; top: 122px;
    width: 196px;
    flex-direction: column; align-items: flex-start; gap: 6px;
    color: var(--red);
  }
  .card-contact .brand-row { display: flex; align-items: center; gap: 7px; }
  .card-contact .brand-mark { width: 10px; height: 10px; }
  .card-contact .brand-name { font-size: 16px; letter-spacing: 0.3px; }
  .brand-sub { font-size: 10px; letter-spacing: 4px; padding-left: 17px; }

  .divider {
    position: absolute;
    left: 236px; top: 60px;
    width: 1.5px; height: 190px;
    background: var(--red);
  }
  .person { position: absolute; left: 256px; top: 60px; }
  .person-name { color: var(--red); font-size: 21px; font-weight: 700; line-height: 1.1; }
  .person-role { font-size: 13px; margin-top: 2px; }

  .contacts {
    position: absolute;
    left: 256px; top: 130px;
    list-style: none;
    font-size: 12.5px;
  }
  .contacts li { display: flex; align-items: center; gap: 8px; height: 22px; }
  .contacts svg { width: 13px; height: 13px; flex: none; }
</style>
</head>
<body>

  <section class="card card-appointment">
    <div class="brand">
      <span class="brand-mark"></span>
      <span class="brand-name">Ridgeback Prime</span>
    </div>

    <ul class="services">
      <li>Vehicle Servicing</li>
      <li>All Mechanical Repairs</li>
      <li>Warrant of Fitness</li>
      <li>Tyres &amp; Wheel Alignments</li>
      <li>Automotive Diagnostics</li>
      <li>Automotive Parts &amp; Supplies</li>
    </ul>

    <h2 class="appointment-title">APPOINTMENT</h2>

    <div class="field field-name"><span>Name:</span><span class="line"></span></div>
    <div class="field field-time"><span>Time:</span><span class="line"></span></div>
    <div class="ampm"><span class="check">AM</span><span class="check">PM</span></div>
    <div class="field field-date"><span>Date:</span><span class="line"></span></div>

    <div class="days">
      <span class="check">Mon</span>
      <span class="check">Tues</span>
      <span class="check">Wed</span>
      <span class="check">Thur</span>
      <span class="check">Fri</span>
      <span class="check">Sat</span>
    </div>

    <div class="notice-band">If you are unable to keep your appointment, please call us within 24 hours.</div>
  </section>

  <section class="card card-contact">
    <div class="brand">
      <div class="brand-row">
        <span class="brand-mark"></span>
        <span class="brand-name">Ridgeback Prime</span>
      </div>
      <span class="brand-sub">Automotive</span>
    </div>

    <div class="divider"></div>

    <div class="person">
      <div class="person-name">Lachie Westergaard</div>
      <div class="person-role">Director</div>
    </div>

    <ul class="contacts">
      <li>
        <svg viewBox="0 0 16 16" fill="none" stroke="#d71f27" stroke-width="1.6"><path d="M8 15s5-5 5-8.5A5 5 0 0 0 3 6.5C3 10 8 15 8 15z"/><circle cx="8" cy="6.5" r="1.8"/></svg>
        48 Marlow Lane, Whitianga 3510
      </li>
      <li>
        <svg viewBox="0 0 16 16" fill="#d71f27"><path d="M3.5 1.5l2.5 0 1 3.5-1.7 1.2a8 8 0 0 0 4.5 4.5L11 9l3.5 1v2.5c0 1-1 2-2 2C7 14.5 1.5 9 1.5 3.5c0-1 1-2 2-2z"/></svg>
        07 842 1937
      </li>
      <li>
        <svg viewBox="0 0 16 16" fill="none" stroke="#d71f27" stroke-width="1.6"><rect x="4" y="1" width="8" height="14" rx="1.5"/><line x1="7" y1="12.5" x2="9" y2="12.5"/></svg>
        027 519 2764
      </li>
      <li>
        <svg viewBox="0 0 16 16" fill="none" stroke="#d71f27" stroke-width="1.6"><rect x="1.5" y="3.5" width="13" height="9"/><path d="M1.5 3.5L8 9l6.5-5.5"/></svg>
        office@ridgebackmotors.co.nz
      </li>
      <li>
        <svg viewBox="0 0 16 16" fill="none" stroke="#d71f27" stroke-width="1.4"><circle cx="8" cy="8" r="6.5"/><ellipse cx="8" cy="8" rx="3" ry="6.5"/><line x1="1.5" y1="8" x2="14.5" y2="8"/></svg>
        ridgebackmotors.co.nz
      </li>
    </ul>
  </section>

</body>
</html>
```